Business Card Design (NEW FILES)

ATTENTION: New vector files are available. Please update your design to reflect/use the new (better resolution) logo images.

Seeking a unique and professional business card design for a commercial drone photography/videography business. The layout should feature
the logo (attached) and include the following information:
Pete Varner
978-552-6170
www.skylarkvisuals.example
NVR Certified Remote Pilot

Pete Varner

```html
<!DOCTYPE html>
<html lang="en">
<head>
<meta charset="utf-8">
<title>Skylark Visuals – Business Card</title>
<link href="https://fonts.googleapis.com/css2?family=Poppins:ital,wght@0,300;0,400;0,500;0,700;1,500&display=swap" rel="stylesheet">
<style>
  :root {
    --navy: #161a4d;
    --orange: #ec8a4c;
    --white: #ffffff;
    --ghost: #ececec;
    --stage: #3a3a3a;
    --rule: #1f2460;
  }
  * { box-sizing: border-box; margin: 0; padding: 0; }
  html, body { width: 1200px; height: 866px; overflow: hidden; }
  body {
    background: var(--stage);
    font-family: "Poppins", sans-serif;
    display: flex;
    align-items: center;
    justify-content: center;
    gap: 40px;
  }
  .card {
    position: relative;
    width: 540px;
    height: 309px;
    overflow: hidden;
    box-shadow: 0 10px 24px rgba(0,0,0,.45);
  }
  .card--front { background: var(--white); }
  .card--back { background: var(--navy); }

  .backdrop-art {
    position: absolute;
    left: 0; top: 0;
    width: 300px; height: 200px;
    background: radial-gradient(ellipse at 40% 35%, var(--ghost) 0%, rgba(236,236,236,0.5) 45%, rgba(255,255,255,0) 75%);
  }

  .contact {
    position: absolute;
    left: 34px; top: 78px;
    color: var(--navy);
  }
  .contact__name {
    font-weight: 700;
    font-size: 24px;
    letter-spacing: 1px;
    line-height: 1;
  }
  .contact__role {
    font-weight: 400;
    font-size: 13px;
    color: var(--orange);
    letter-spacing: 1px;
    margin-top: 3px;
    padding-bottom: 8px;
    border-bottom: 1px solid var(--rule);
    width: 200px;
  }
  .contact__row {
    display: flex;
    align-items: center;
    gap: 8px;
    font-size: 12.5px;
    margin-top: 8px;
    letter-spacing: .3px;
  }
  .contact__row svg { width: 13px; height: 13px; flex: none; }

  .brand {
    position: absolute;
    display: flex;
    align-items: center;
    justify-content: center;
    gap: 10px;
  }
  .brand__name {
    font-weight: 400;
    letter-spacing: 2px;
    line-height: 1;
    white-space: nowrap;
  }
  .brand__dot { border-radius: 50%; flex: none; background: var(--orange); }

  .card--front .brand { right: 26px; top: 100px; width: 250px; }
  .card--front .brand__name { color: var(--navy); font-size: 21px; }
  .card--front .brand__dot { width: 12px; height: 12px; }

  .divider {
    position: absolute;
    left: 34px; right: 34px; top: 215px;
    border-top: 1px solid var(--rule);
  }

  .footer-band { position: absolute; left: 0; bottom: 0; width: 540px; height: 60px; }
  .footer-band__text {
    position: absolute;
    right: 26px; bottom: 9px;
    color: var(--white);
    font-style: italic;
    font-weight: 500;
    font-size: 13px;
    text-align: right;
    line-height: 1.35;
    letter-spacing: .5px;
  }

  .card--back .brand {
    left: 0; right: 0; top: 50%;
    transform: translateY(-50%);
  }
  .card--back .brand__name { color: var(--white); font-size: 36px; }
  .card--back .brand__dot { width: 18px; height: 18px; }
</style>
</head>
<body>

<section class="card card--front">
  <div class="backdrop-art" role="img" aria-label="Faint drone illustration in the background"></div>

  <div class="contact">
    <p class="contact__name">PETE VARNER</p>
    <p class="contact__role">OWNER</p>
    <p class="contact__row">
      <svg viewBox="0 0 16 16" aria-hidden="true"><path d="M3.5 1.5l2.5 0.5 1 3-1.7 1.3a9 9 0 0 0 4.4 4.4L11 9l3 1 .5 2.5-1.8 1.8C7.5 14 2 8.5 1.7 3.3z" fill="var(--navy)"/></svg>
      978-552-6170
    </p>
    <p class="contact__row">
      <svg viewBox="0 0 16 16" aria-hidden="true"><g fill="none" stroke="var(--navy)" stroke-width="1.4"><circle cx="8" cy="8" r="6.5"/><ellipse cx="8" cy="8" rx="2.8" ry="6.5"/><path d="M1.5 8h13M2.5 4.8h11M2.5 11.2h11"/></g></svg>
      www.skylarkvisuals.example
    </p>
  </div>

  <div class="brand">
    <span class="brand__name">SKYLARK VISUALS</span>
    <span class="brand__dot"></span>
  </div>

  <div class="divider"></div>

  <svg class="footer-band" viewBox="0 0 540 60" aria-hidden="true">
    <rect x="0" y="32" width="200" height="3" fill="var(--orange)"/>
    <rect x="0" y="35" width="200" height="25" fill="var(--navy)"/>
    <path d="M150 35 C190 35 200 8 245 8 L540 8 L540 60 L150 60 Z" fill="var(--navy)"/>
  </svg>
  <p class="footer-band__text">NVR Certified Remote Pilot<br>Fully Insured</p>
</section>

<section class="card card--back">
  <div class="brand">
    <span class="brand__name">SKYLARK VISUALS</span>
    <span class="brand__dot"></span>
  </div>
</section>

</body>
</html>
```